Bref créative
Professional website for IT consultancy firm
Vela Tundo
Consulting
www.velatundo.example
About Vela Tundo Consultants
Vela Tundo Consultants was created in 2012 by our five founding partners as a response to the demand in the market for a single organization that could provide high quality experienced KEL consultants with extensive industry knowledge.
Each of our managing directors has over a decade of local and international KEL implementation experience in the Oil & Gas industry. Throughout their careers they have personally worked with hundreds of independent consultants and know who the high quality performers are. In order to maintain Vela Tundo’s high quality level, consultants only work through Vela Tundo upon invitation or recommendation.
Vela Tundo works jointly with the Top-6 consulting firms and other system integrators during KEL implementations, providing hard to find quality resources, as well as directly with our end clients either in an implementation lead role or a resourcing support capacity.
Corporate
Blue C=85 M=50 Y=0 K=40
Grey C=0 M=0 Y=0 K=90
brixmoorlink.example
pendrik.example
www.halvanosys.example
Company Logo
Back side of Business Card

```html
<!DOCTYPE html>
<html lang="en">
<head>
<meta charset="utf-8">
<title>Vela Tundo Consulting</title>
<link href="https://fonts.googleapis.com/css2?family=Arimo:ital,wght@0,400;0,700;1,400;1,700&display=swap" rel="stylesheet">
<style>
:root{
  --brand-blue:#0b4f8f;
  --brand-blue-light:#3a86c8;
  --ink:#1a1a1a;
  --grey-dark:#2b2b2b;
  --grey-mid:#5a5a5a;
  --grey-light:#e9ecef;
  --line:#cfd5db;
  --white:#ffffff;
}
*{box-sizing:border-box;margin:0;padding:0}
html,body{width:1200px;height:1110px;overflow:hidden;background:var(--white);font-family:"Arimo",Arial,sans-serif;color:var(--ink)}
.page{position:relative;width:1200px;height:1110px;overflow:hidden}
.top-band{position:absolute;left:0;top:0;width:1200px;height:570px;background:linear-gradient(#ffffff 0,#f4f6f8 20%,#e6eaee 100%)}
.logo{position:absolute;left:126px;top:28px;display:flex;align-items:center;gap:12px}
.logo-mark{width:42px;height:42px;background:var(--brand-blue)}
.logo-name{font-size:44px;font-weight:700;color:var(--brand-blue);letter-spacing:-1px}
.support{position:absolute;left:800px;top:40px;font-size:15px;font-weight:700;font-style:italic;color:var(--grey-dark)}
.contact-top{position:absolute;left:928px;top:22px;text-align:left}
.contact-top .phone{font-size:32px;font-style:italic;color:var(--brand-blue);line-height:36px}
.contact-top .mail{font-size:15px;font-style:italic;color:var(--brand-blue);border-top:2px solid var(--line);padding-top:2px}
.nav{position:absolute;left:120px;top:108px;width:966px;height:38px;background:linear-gradient(#3a3a3a,#141414);border-radius:3px;display:flex;align-items:center}
.nav a{color:var(--white);text-decoration:none;font-size:15px;padding:0 24px;height:38px;line-height:38px;border-right:1px solid #444}
.nav a.active{background:linear-gradient(#6a6a6a,#3a3a3a);border-radius:3px 0 0 3px}
.search{position:absolute;right:8px;top:5px;width:220px;height:28px;background:var(--white);border-radius:3px;font-size:13px;line-height:28px;padding-left:8px;color:var(--grey-dark)}
.search svg{position:absolute;right:8px;top:5px}
.hero{position:absolute;left:120px;top:159px;width:960px;height:375px;border:6px solid #cfe0ef;border-radius:14px;overflow:hidden;background:linear-gradient(#ffffff,#eef2f6);box-shadow:0 2px 8px rgba(0,0,0,.15)}
.hero svg.swoosh{position:absolute;left:0;top:0}
.hero-photo{position:absolute;left:450px;top:0;width:510px;height:363px;background:linear-gradient(120deg,#d9dfe6 0%,#b7c0c9 45%,#4a4f57 100%)}
.hero-text{position:absolute;left:30px;top:70px;width:420px;font-size:24px;font-weight:700;color:var(--brand-blue);line-height:30px}
.btn{position:absolute;left:30px;top:185px;width:105px;height:40px;background:linear-gradient(#4a4a4a,#1c1c1c);color:var(--white);font-size:14px;line-height:40px;text-align:center;border-radius:3px}
.welcome{position:absolute;left:126px;top:585px;font-size:34px;color:var(--brand-blue)}
.welcome b{font-weight:700}
.divider{position:absolute;left:126px;top:640px;width:948px;height:2px;background:var(--line)}
.col{position:absolute;top:672px;width:296px}
.col-head{position:relative;height:48px;background:linear-gradient(#4a4a4a,#1e1e1e);border-radius:4px;overflow:hidden}
.col-head span{position:absolute;right:22px;top:13px;color:var(--white);font-size:19px;font-style:italic}
.col-head svg{position:absolute;left:0;top:0}
.col p{font-size:13px;line-height:16px;color:var(--ink);margin-top:12px}
.col p.lead{font-weight:700}
.footer{position:absolute;left:0;top:954px;width:1200px;height:156px;background:#1b1b1b}
.footer svg{position:absolute;left:0;top:0}
.foot-links{position:absolute;left:132px;top:84px;font-size:13px;color:var(--white)}
.foot-links span{margin-right:16px}
.foot-copy{position:absolute;left:132px;top:102px;font-size:12px;color:#cfcfcf}
.social{position:absolute;top:72px;width:36px;height:36px;border-radius:50%;background:var(--brand-blue-light);border:2px solid var(--white)}
</style>
</head>
<body>
<div class="page">
  <div class="top-band"></div>
  <div class="logo"><div class="logo-mark"></div><div class="logo-name">VelaTundo</div></div>
  <div class="support">Support Center</div>
  <div class="contact-top"><div class="phone">123-456-789</div><div class="mail">support@velatundo.example</div></div>

  <nav class="nav">
    <a class="active">Home</a><a>About Us</a><a>Management Team</a><a>Services</a><a>Career</a><a>Contact us</a>
    <div class="search">Search Something
      <svg width="18" height="18" viewBox="0 0 18 18"><circle cx="7" cy="7" r="5" fill="none" stroke="#222" stroke-width="2"/><line x1="11" y1="11" x2="16" y2="16" stroke="#222" stroke-width="2.5"/></svg>
    </div>
  </nav>

  <section class="hero">
    <svg class="swoosh" width="948" height="363" viewBox="0 0 948 363">
      <path d="M0 300 C200 200 380 200 520 270 L520 363 L0 363Z" fill="#d5e2ee"/>
      <path d="M0 330 C220 230 400 230 560 300" fill="none" stroke="#5f9dd3" stroke-width="6"/>
    </svg>
    <div class="hero-photo" role="img" aria-label="Three smiling business consultants in suits standing together"></div>
    <div class="hero-text">We provide high quality experienced KEL consultants with extensive industry knowledge.</div>
    <div class="btn">Read More</div>
  </section>

  <h1 class="welcome">Welcome to <b>VelaTundo</b></h1>
  <div class="divider"></div>

  <div class="col" style="left:126px">
    <div class="col-head"><svg width="296" height="48"><path d="M0 48 C60 20 120 8 160 0 L0 0Z" fill="#1f6bb3"/></svg><span>About Us</span></div>
    <p class="lead">Lorem ipsum dolor sit amet, libero turpis non cras ligulaaenean enim. Rimentum vesiblus. Sit non mattis a, leo in imperdiet erat nec pulvinar.</p>
    <p>Felis posuere metus, ornare pede montes, morbi urna sed temporibus non, nibh inceptos enim turpis natoque ac praesent. Libra vivamus veritate est nommy, ut qui est pellentesque at alias, sed condimentum dapibus. Rhoncus lacinia.</p>
  </div>
  <div class="col" style="left:447px">
    <div class="col-head"><svg width="296" height="48"><path d="M0 48 C60 20 120 8 160 0 L0 0Z" fill="#1f6bb3"/></svg><span>Our Services</span></div>
    <p class="lead">Condimentum aliquam, mollit magna velit nec, tempor cursus vitae sit aliquet neque purus. Rimentum vesiblus. Sit non mattis a, leo in imperdiet erat nec pulvinar.</p>
    <p>Nibh inceptos enim turpis natoque ac praesent. Libra vivamus veritate est nommy, ut qui est pellentesque at alias, sed condimentum dapibus. Rhoncus lacinia.</p>
  </div>
  <div class="col" style="left:768px">
    <div class="col-head"><svg width="296" height="48"><path d="M0 48 C60 20 120 8 160 0 L0 0Z" fill="#1f6bb3"/></svg><span>Our Services</span></div>
    <p class="lead">Rimentum vesiblus. Sit non mattis a, leo in imperdiet erat nec pulvinar. Felis posuere metus, ornare pede montes, morbi urna sed temporibus non dapibus.</p>
    <p>1123 Marlow Way<br>Orvenne County, 112233</p>
    <p>Phone : 123 456 789<br>Fax : 123 456 789<br>Email : support@velatundo.example</p>
  </div>

  <footer class="footer">
    <svg width="1200" height="70" viewBox="0 0 1200 70">
      <rect width="1200" height="70" fill="#ffffff"/>
      <path d="M0 30 C300 0 600 60 900 40 C1050 30 1150 10 1200 20 L1200 70 L0 70Z" fill="#1f6bb3"/>
      <path d="M0 46 C300 20 600 72 900 56 C1050 48 1150 30 1200 38 L1200 70 L0 70Z" fill="#1b1b1b"/>
    </svg>
    <div class="foot-links"><span>Home</span>|&nbsp;&nbsp;&nbsp;<span>Terms &amp; Conditions</span>|&nbsp;&nbsp;&nbsp;<span>FAQ</span>|&nbsp;&nbsp;&nbsp;<span>Privacy Policy</span></div>
    <div class="foot-copy">Copyright © 2012 velatundo.example</div>
    <div class="social" style="left:936px"></div>
    <div class="social" style="left:986px"></div>
    <div class="social" style="left:1036px"></div>
  </footer>
</div>
</body>
</html>
```